The Lanterns of Steady Craft Personal Growth Template

We are creating a two-page Word document titled 'The Lanterns of Steady Craft.' This guide/template should embody a professional, clear, and engaging design that facilitates learning and application of DEI principles within a business context.

Target Market(s)

Our primary users are middle to senior management professionals who are responsible for implementing and upholding DEI values within their teams and organizations. The design must resonate with this demographic, implying a sophisticated and functional aesthetic.

Industry/Entity Type

Healthcare, Counseling

Requirements
Must have
• Branding: Incorporate BRK colors for branding consistency. Ensure that the 'Lanterns of Steady Craft' is prominently featured within the design. Content Layout: We require a clean, clear, and logical layout that intuitively guides the user through the steps of the DEI Growth Matrix. Image Redesign: The images pertaining to the assessment and differentiation of self should be recreated to be high-resolution and professionally styled. They should directly support the content and be relatable to our target audience. Accessibility: The template must be easily navigable, with font sizes and styles that ensure readability and ADA compliance. Actionable Steps: Clearly define sections for 'Inspiration,' 'Goal,' and 'Daily Commitment' with examples provided, and allow for user interaction such as note-taking or checkboxes. Reflection Section: Include a 'Two-Week Reflection & Follow-up' section to encourage ongoing engagement with the tool.
Nice to have
• we would appreciate it if the 'Daily Biopsychosocial Commitment Table' could be adjusted to track actions over a four-week period, rather than daily, to align with managerial workflows.
Should not have
• Informal Graphics: Avoid the use of cartoons, silly icons, or figures that could detract from the professional tone of the document. Overcrowding: Prevent a cluttered design by balancing white space with content, ensuring the guide does not overwhelm the user.

```html
<!DOCTYPE html>
<html lang="en">
<head>
<meta charset="utf-8">
<title>DEI Growth Matrix — The Lanterns of Steady Craft</title>
<link rel="stylesheet" href="https://fonts.googleapis.com/css2?family=Montserrat:wght@400;500;600;700;800&display=swap">
<style>
:root{
  --navy:#2a2866;
  --gold:#b5893a;
  --violet:#5852ad;
  --grey:#ececef;
  --cream:#efe4d2;
  --ink:#2b2b3a;
  --bg:#d6d6d6;
  --lav:#c9c6f5;
  --lav-2:#e6e4fb;
  --peach:#f6e6d3;
  --peach-2:#f9d8ac;
  --sky:#dbeafb;
  --sky-2:#e9f2fc;
  --social-blue:#6f8fd3;
}
*{box-sizing:border-box;margin:0;padding:0}
html,body{width:1200px;height:2400px;overflow:hidden}
body{background:var(--bg);font-family:"Montserrat",Arial,sans-serif;color:var(--ink);position:relative}
.page{position:absolute;left:80px;width:1040px;height:807px;background:#fff;box-shadow:0 4px 10px rgba(0,0,0,.25);overflow:hidden}
.page--matrix{top:200px}
.page--table{top:1230px}

/* masthead */
.masthead{position:absolute;left:0;top:0;width:1040px;height:118px}
.masthead svg{position:absolute;left:0;top:0}
.brand{position:absolute;left:20px;top:30px;width:150px;text-align:center}
.brand__dot{width:44px;height:44px;border:2px solid var(--navy);border-radius:50%;margin:0 auto 5px}
.brand__name{font-size:11px;font-weight:700;color:var(--navy);line-height:1.2}
.title{position:absolute;left:252px;top:30px;font-size:40px;font-weight:800;letter-spacing:9px;color:var(--gold);line-height:1}
.subtitle{position:absolute;left:252px;top:80px;font-size:21px;font-weight:500;color:#fff;letter-spacing:.3px;white-space:nowrap}

.purpose{position:absolute;left:34px;top:134px;width:965px;height:44px;border:2px solid var(--gold);border-radius:6px;display:flex;align-items:center;overflow:hidden}
.purpose__label{background:var(--gold);color:#fff;font-weight:700;font-size:15px;height:100%;width:104px;flex:none;display:flex;align-items:center;justify-content:center}
.purpose__text{font-size:13.5px;padding:0 12px;line-height:1.2}
.tag{position:absolute;background:var(--navy);color:#fff;font-weight:600;font-size:13px;padding:2px 6px;border-radius:2px}
.tag--instr{left:34px;top:185px}

.step{position:absolute;border:2px solid var(--navy);border-radius:8px;padding:26px 11px 8px}
.step__head{position:absolute;top:-2px;left:50%;transform:translateX(-50%);background:var(--navy);color:#fff;font-weight:700;font-size:13px;padding:3px 26px;border-radius:0 0 6px 6px;white-space:nowrap}
.step__head em{font-style:normal;color:var(--gold)}
.step__intro{font-size:10px;line-height:1.3}
.step__lead{font-size:10.5px;font-weight:700;color:var(--navy);margin-top:6px}
.step__lead-sub{font-size:10px;color:var(--gold);margin-top:1px}
.step--inspire{left:36px;top:212px;width:467px;height:292px}
.step--goal{left:530px;top:212px;width:469px;height:292px}
.step--commit{left:34px;top:516px;width:965px;height:200px}

.triad{display:grid;grid-template-columns:repeat(3,1fr);margin-top:6px;font-size:8.5px;line-height:1.2;height:196px}
.triad__col{background:var(--grey);padding:0 6px 6px}
.triad__col:nth-child(2){background:var(--cream)}
.triad__head{margin:0 -6px 8px;color:#fff;text-align:center;font-weight:700;font-size:13px;padding:1px 0}
.triad__head--bio{background:var(--navy)}
.triad__head--psycho{background:var(--gold)}
.triad__head--social{background:var(--violet)}
.triad .triad__head--social{border-radius:0 6px 0 0}
.triad__col p{margin-bottom:12px}

.goal-grid{display:grid;grid-template-columns:174px 82px 173px;gap:6px;margin-top:6px;font-size:8px;line-height:1.15}
.goal-card{background:var(--grey);border-radius:0 0 6px 6px;height:186px}
.goal-card__head{color:#fff;font-weight:700;font-size:9.5px;padding:3px 8px;line-height:1.1}
.goal-card__head--navy{background:var(--navy);clip-path:polygon(0 0,88% 0,100% 100%,0 100%)}
.goal-card__head--gold{background:var(--gold);clip-path:polygon(12% 0,100% 0,100% 100%,0 100%);text-align:center}
.ticks{list-style:none;padding:6px 6px 0}
.ticks li{padding-left:12px;position:relative;margin-bottom:3px}
.ticks li::before{content:"";position:absolute;left:0;top:1px;width:7px;height:7px;border:1px solid #666;border-radius:50%}
.goal-photo{border-radius:6px;height:186px;background:linear-gradient(160deg,#e9edf3 0%,#9aa3b0 55%,#3b3d48 100%)}

.commit-intro{font-size:10px;margin:0 14px}
.commit-grid{display:grid;grid-template-columns:repeat(3,1fr);margin:7px 10px 0;font-size:8.5px;line-height:1.22}
.commit-col{background:var(--grey);padding:0 6px 6px}
.commit-col:nth-child(2){background:var(--cream)}
.commit-col .triad__head{margin:0 -6px 4px;font-size:13px;padding:3px 0}
.commit-col__lead{padding-bottom:5px;border-bottom:1px solid #fff}
.commit-col__ex{color:var(--navy);font-weight:600;font-size:9.5px;margin-top:4px}
.commit-col .ticks{padding:2px 0 0}

.reflect{position:absolute;left:34px;top:728px;width:828px;height:50px;border:2px solid var(--navy);border-radius:6px}
.reflect__head{position:absolute;left:-2px;top:-2px;background:#fff;font-weight:700;font-size:12.5px;color:var(--navy);padding:2px 12px;border-bottom:2px solid var(--navy);border-right:2px solid var(--navy);border-radius:6px 0 6px 0}
.reflect__head em{font-style:normal;color:var(--gold)}
.partner{position:absolute;left:880px;top:730px;width:140px;text-align:center}
.partner__dot{width:28px;height:28px;border:2px solid var(--gold);border-radius:50%;margin:0 auto 4px}
.partner__name{font-size:9.5px;font-weight:700;color:var(--navy)}

/* table page */
.tbl-title{position:absolute;left:36px;top:48px;font-size:15px;font-weight:700;color:#fff;letter-spacing:4px;white-space:nowrap}
.tbl-cols{position:absolute;top:92px;left:34px;right:41px;height:20px;display:flex}
.tbl-cols__action{width:330px;background:var(--navy);color:#fff;font-size:10.5px;font-weight:600;display:flex;align-items:center;justify-content:center;white-space:nowrap}
.tbl-cols__days{margin-left:17px;flex:1;display:grid;grid-template-columns:repeat(7,1fr);gap:2px}
.day{color:#fff;font-size:11px;font-weight:600;display:flex;align-items:center;justify-content:center}
.day:nth-child(odd){background:var(--violet)}
.day:nth-child(even){background:var(--gold)}

.group{position:absolute;left:34px;width:965px;height:204px;border:2px solid;border-radius:8px;overflow:hidden;display:grid;grid-template-columns:347px 1fr}
.group--bio{top:126px;border-color:var(--violet)}
.group--psycho{top:346px;border-color:var(--gold)}
.group--social{top:566px;border-color:#7f9ddc}
.group__tag{position:absolute;left:0;top:0;color:#fff;font-weight:700;font-size:14px;padding:0 18px;z-index:1;border-radius:0 0 8px 0;line-height:19px}
.group--bio .group__tag{background:var(--navy)}
.group--psycho .group__tag{background:var(--gold)}
.group--social .group__tag{background:var(--social-blue)}
.actions{display:grid;grid-template-rows:repeat(3,1fr)}
.action{display:flex;align-items:center;gap:14px;padding:8px 12px 0;border-bottom:1px solid #fff;font-size:9.5px;font-weight:600;text-transform:uppercase;line-height:1.25;white-space:nowrap}
.action:first-child{padding-top:20px}
.group--bio .action{background:var(--grey)}
.group--psycho .action{background:#f6efe6}
.group--social .action{background:var(--grey)}
.action:last-child{border-bottom:0}
.action__no{font-size:16px;font-weight:700;width:12px;flex:none}
.group--bio .action__no{color:var(--navy)}
.group--psycho .action__no{color:var(--gold)}
.group--social .action__no{color:var(--social-blue)}
.cells{display:grid;grid-template-columns:repeat(7,1fr);grid-template-rows:repeat(3,1fr)}
.cell{border-right:1px solid #fff;border-bottom:1px solid #fff}
.group--bio .cell{background:repeating-linear-gradient(180deg,var(--lav) 0 17px,var(--lav-2) 17px 34px)}
.group--psycho .cell{background:var(--peach)}
.group--psycho .cell--done{background:repeating-linear-gradient(180deg,var(--peach-2) 0 17px,#fbeedd 17px 34px)}
.group--psycho .cell:nth-child(7n+4),.group--psycho .cell:nth-child(7n+6){background:#f2ece6}
.group--social .cell{background:var(--sky)}
.group--social .cell:nth-child(even){background:var(--sky-2)}
</style>
</head>
<body>

<section class="page page--matrix" aria-label="DEI Growth Matrix">
  <header class="masthead">
    <svg width="1040" height="118" viewBox="0 0 1040 118">
      <rect x="0" y="0" width="1040" height="6" fill="var(--navy)"/>
      <polygon points="168,6 1040,6 1040,118 240,118" fill="var(--navy)"/>
      <polygon points="168,6 176,6 248,112 1040,112 1040,116 244,116" fill="var(--gold)"/>
    </svg>
    <div class="brand"><div class="brand__dot"></div><div class="brand__name">The Lanterns of Steady Craft</div></div>
    <h1 class="title">DEI GROWTH MATRIX</h1>
    <p class="subtitle">A BIOPSYCHOSOCIAL &amp; DIFFERENTIATION FRAMEWORK</p>
  </header>

  <div class="purpose"><span class="purpose__label">PURPOSE</span><p class="purpose__text">This template is designed to help individuals integrate DEI principles into their professional lives by identifying and committing to personal growth areas aligned with Systems and Bowen Theory.</p></div>
  <span class="tag tag--instr">INSTRUCTIONS</span>

  <div class="step step--inspire">
    <div class="step__head">STEP 1: <em>INSPIRATION</em></div>
    <p class="step__intro">Examine the bio-psycho-social assessment and identify areas to improve your ability to contribute to a DEI-focused work environment.</p>
    <p class="step__lead">LEADERS RENEW SPIRIT, BUILD RESILIENCE AND FOSTER WELL-BEING</p>
    <div class="triad">
      <div class="triad__col"><div class="triad__head triad__head--bio">BIO</div>
        <p>I am aware of how family, culture, and experiences affect how I think &amp; behave.</p>
        <p>I am aware of neuro diversity and how to leverage it for success.</p>
        <p>I nurture body and spirit in a manner that fosters hope, empathy, and grace.</p></div>
      <div class="triad__col"><div class="triad__head triad__head--psycho">PSYCHO</div>
        <p>I foster a psychologically safe environment to acknowledge, discuss &amp; address emotional and polarizing issues.</p>
        <p>I instill the confidence that views and perspectives will be acknowledged and considered</p>
        <p>I am aware of unique talent(s), or strength(s) and how to nurture them.</p></div>
      <div class="triad__col"><div class="triad__head triad__head--social">SOCIAL</div>
        <p>I consistently find ways to show appreciation during stressful and uncertain situations.</p>
        <p>I cultivate a broad and culturally diverse network of individuals to exchange ideas and make decisions.</p>
        <p>I use my power in visible and subtle ways to include people and discourage exclusion.</p></div>
    </div>
  </div>

  <div class="step step--goal">
    <div class="step__head">STEP 2: <em>GOAL</em></div>
    <p class="step__intro">Choose attributes from the 'Differentiation of Self' framework that will support your role in fostering a DEI culture at work.</p>
    <p class="step__lead">DIFFERENTIATION OF SELF (FOSTERING UNIQUENESS)</p>
    <p class="step__lead-sub">How do we foster "differentiation of self for ourselves and others?</p>
    <div class="goal-grid">
      <div class="goal-card"><div class="goal-card__head goal-card__head--navy">"Differentiation of Self"<br>Characteristics</div>
        <ul class="ticks"><li>Be an interdependent member of the group.</li><li>Maintain beliefs and attitudes in the face of pressure to conform</li><li>Resolve problems rather than let them fester.</li><li>Self-validate</li><li>Self-soothe</li><li>Tolerate short-term discomfort or gratification for long-term growth</li><li>Taking action</li></ul></div>
      <div class="goal-photo" role="img" aria-label="Photo of a professional presenting a chart to seated colleagues"></div>
      <div class="goal-card"><div class="goal-card__head goal-card__head--gold">"Differentiation of Self"<br>Benefits</div>
        <ul class="ticks"><li>A sense of congruence within yourself - pride &amp; confidence</li><li>Highly self-aware-greater capacity to be aware of others</li><li>Highly differentiated better at handling stress/anxiety</li><li>Positive feelings can become self-perpetuating</li><li>Increased differentiation by one members to become more differentiated</li><li>Ownership of self</li></ul></div>
    </div>
  </div>

  <div class="step step--commit">
    <div class="step__head">STEP 3: <em>DAILY COMMITMENT</em></div>
    <p class="commit-intro">Define specific, daily actions to help you work towards your well-being and differentiation goals, ultimately enhancing DEI implementation in your job.</p>
    <div class="commit-grid">
      <div class="commit-col"><div class="triad__head triad__head--bio">BIO</div>
        <p class="commit-col__lead">In the 'Bio' category, actions could include self-care practices that enable one to be an effective DEI advocate even under stress.</p>
        <p class="commit-col__ex">Examples include</p>
        <ul class="ticks"><li>Practice mindfulness to maintain resilience when discussing DEI topics in polarized settings.</li><li>Engage in physical activities that improve mental clarity to approach DEI work with a non-anxious presence.</li></ul></div>
      <div class="commit-col"><div class="triad__head triad__head--psycho">PSYCHO</div>
        <p class="commit-col__lead">'Psycho' actions may involve education and reflection on one's cultural competencies and biases</p>
        <p class="commit-col__ex">Examples include</p>
        <ul class="ticks"><li>Reflect daily on personal biases to foster a mindset open to DEI learning and transformation.</li><li>Write a journal about DEI progress to reinforce learning and personal growth in DEI competencies.</li></ul></div>
      <div class="commit-col"><div class="triad__head triad__head--social">SOCIAL</div>
        <p class="commit-col__lead">'Social' commitments could be activities that promote inclusion and equity within one's immediate professional sphere.</p>
        <p class="commit-col__ex">Examples include</p>
        <ul class="ticks"><li>Initiate conversations about DEI with colleagues to understand diverse perspectives.</li><li>Lead by example in inclusive behaviors, ensuring all team members feel valued and heard.</li></ul></div>
    </div>
  </div>

  <div class="reflect"><span class="reflect__head">TWO-WEEK REFLECTION &amp; <em>FOLLOW</em></span></div>
  <div class="partner"><div class="partner__dot"></div><div class="partner__name">BROOKLINE REACH GROUP</div></div>
</section>

<section class="page page--table" aria-label="Daily Biopsychosocial Commitment Table">
  <header class="masthead">
    <svg width="1040" height="90" viewBox="0 0 1040 90">
      <rect x="0" y="0" width="1040" height="6" fill="var(--navy)"/>
      <polygon points="0,6 680,6 630,78 0,78" fill="var(--navy)"/>
      <polygon points="686,6 694,6 640,82 0,82 0,79 633,79" fill="var(--gold)"/>
    </svg>
    <h2 class="tbl-title">DAILY BIOPSYCHOSOCIAL COMMITMENT TABLE</h2>
  </header>

  <div class="tbl-cols">
    <div class="tbl-cols__action">ACTION / THE DAY ACTION WAS TAKEN OVER 4 WEEKS</div>
    <div class="tbl-cols__days">
      <span class="day">MONDAY</span><span class="day">TUESDAY</span><span class="day">WEDNESDAY</span><span class="day">THURSDAY</span><span class="day">FRIDAY</span><span class="day">SATURDAY</span><span class="day">SUNDAY</span>
    </div>
  </div>

  <div class="group group--bio">
    <span class="group__tag">BIO</span>
    <div class="actions">
      <div class="action"><span class="action__no">1</span><span>Engage in 16-8 intermittent<br>fasting to address GERD</span></div>
      <div class="action"><span class="action__no">2</span><span>Complete 28-day body-weight<br>strength training</span></div>
      <div class="action"><span class="action__no">3</span><span>Incorporate daily natto<br>into daily diet</span></div>
    </div>
    <div class="cells">
      <i class="cell"></i><i class="cell"></i><i class="cell"></i><i class="cell"></i><i class="cell"></i><i class="cell"></i><i class="cell"></i>
      <i class="cell"></i><i class="cell"></i><i class="cell"></i><i class="cell"></i><i class="cell"></i><i class="cell"></i><i class="cell"></i>
      <i class="cell"></i><i class="cell"></i><i class="cell"></i><i class="cell"></i><i class="cell"></i><i class="cell"></i><i class="cell"></i>
    </div>
  </div>

  <div class="group group--psycho">
    <span class="group__tag">PSYCHO</span>
    <div class="actions">
      <div class="action"><span class="action__no">1</span><span>Complete night neurofeedback digital<br>sleeping pill to improve sleep and underst<br>and neurofeedback coaching</span></div>
      <div class="action"><span class="action__no">2</span><span>Incorporate insight dialogue into<br>client sessions</span></div>
      <div class="action"><span class="action__no">3</span><span>Complete daily morning box-breathing</span></div>
    </div>
    <div class="cells">
      <i class="cell cell--done"></i><i class="cell cell--done"></i><i class="cell cell--done"></i><i class="cell"></i><i class="cell"></i><i class="cell"></i><i class="cell"></i>
      <i class="cell"></i><i class="cell"></i><i class="cell"></i><i class="cell"></i><i class="cell"></i><i class="cell"></i><i class="cell"></i>
      <i class="cell"></i><i class="cell"></i><i class="cell"></i><i class="cell"></i><i class="cell"></i><i class="cell"></i><i class="cell"></i>
    </div>
  </div>

  <div class="group group--social">
    <span class="group__tag">SOCIAL</span>
    <div class="actions">
      <div class="action"><span class="action__no">1</span><span>Join and participate in the<br>Vancouver jazz meet-up</span></div>
      <div class="action"><span class="action__no">2</span><span>Plan 2-annual guys trip with Marcus</span></div>
      <div class="action"><span class="action__no">3</span><span>Plan the annual couples' trip<br>with Marcus &amp; Elena</span></div>
    </div>
    <div class="cells">
      <i class="cell"></i><i class="cell"></i><i class="cell"></i><i class="cell"></i><i class="cell"></i><i class="cell"></i><i class="cell"></i>
      <i class="cell"></i><i class="cell"></i><i class="cell"></i><i class="cell"></i><i class="cell"></i><i class="cell"></i><i class="cell"></i>
      <i class="cell"></i><i class="cell"></i><i class="cell"></i><i class="cell"></i><i class="cell"></i><i class="cell"></i><i class="cell"></i>
    </div>
  </div>
</section>

</body>
</html>
```